Business Card Design Project

I am community manager and social media strategist. I need a double sided business card with company logo and name. Looking for something professional, elegant but also a little bit original.

• - The logo and the colours are the company colours and a required to stay.
- The size should be: 84 x 55 mm (or 3.30 x 2.16)
- The file size should be: 1039 x 697 pixels (300 dpi)
- I'd like rounded corners. :)

Use the following contact information for the card:

Léonie Vardin
Stratégie médias sociaux / community management / édition de sites sociaux
mob. : 0687529103
leonie.vardin@postelune.fr
Twitter. : @lvardin
Skype : vardin.leonie

```html
<!DOCTYPE html>
<html lang="fr">
<head>
<meta charset="utf-8">
<title>Léonie Vardin – carte de visite</title>
<link href="https://fonts.googleapis.com/css2?family=Encode+Sans+Condensed:wght@300;400;500&display=swap" rel="stylesheet">
<style>
  :root {
    --page: #ffffff;
    --card: #5f6062;
    --card-back: #636466;
    --pattern-dark: #4a4b4d;
    --accent: #1e9fd8;
    --text-light: #dcdcdc;
    --shadow: rgba(40, 40, 60, 0.35);
  }
  * { margin: 0; padding: 0; box-sizing: border-box; }
  html, body {
    width: 1200px;
    height: 578px;
    overflow: hidden;
    background: var(--page);
    font-family: "Encode Sans Condensed", "Arial Narrow", sans-serif;
  }
  .canvas { position: relative; width: 1200px; height: 578px; }

  .card {
    position: absolute;
    top: 118px;
    width: 510px;
    height: 334px;
    border-radius: 52px;
    overflow: hidden;
    box-shadow: 3px 4px 6px var(--shadow);
  }
  .card--front { left: 13px; background: var(--card); }
  .card--back  { left: 552px; background: var(--card-back); }

  .holder-name {
    position: absolute;
    left: 70px;
    top: 52px;
    font-size: 27px;
    font-weight: 500;
    color: var(--accent);
  }
  .holder-role {
    position: absolute;
    left: 70px;
    width: 365px;
    top: 98px;
    font-size: 17.5px;
    font-weight: 300;
    color: var(--text-light);
    text-align: center;
    line-height: 38px;
  }
  .divider {
    position: absolute;
    left: 0;
    top: 175px;
    width: 100%;
    height: 1px;
    background: var(--accent);
    opacity: 0.7;
  }
  .brand {
    position: absolute;
    left: 62px;
    top: 198px;
    width: 130px;
    display: flex;
    flex-direction: column;
    align-items: center;
    gap: 12px;
  }
  .brand-dot {
    width: 68px;
    height: 68px;
    border-radius: 50%;
    background: var(--accent);
  }
  .brand-name {
    font-size: 28px;
    font-weight: 500;
    letter-spacing: 2px;
    color: var(--accent);
  }
  .contact {
    position: absolute;
    left: 281px;
    top: 198px;
    list-style: none;
    font-size: 17px;
    font-weight: 300;
    color: var(--text-light);
    line-height: 26px;
  }

  .back-pattern {
    position: absolute;
    inset: 0;
    background: radial-gradient(circle at 50% 50%, var(--card-back) 0%, var(--pattern-dark) 140%);
  }
  .back-brand {
    position: absolute;
    left: 74px;
    top: 138px;
    display: flex;
    align-items: center;
    gap: 12px;
  }
  .back-brand .brand-dot { width: 58px; height: 58px; }
  .back-brand .brand-name { font-size: 26px; }
</style>
</head>
<body>
<main class="canvas">
  <section class="card card--front">
    <h1 class="holder-name">Léonie Vardin</h1>
    <p class="holder-role">Stratégie médias sociaux / community management<br>édition de sites sociaux</p>
    <div class="divider"></div>
    <div class="brand">
      <span class="brand-dot"></span>
      <span class="brand-name">NOVELIA</span>
    </div>
    <ul class="contact">
      <li>Mobile. : 0687529103</li>
      <li>leonie.vardin@postelune.fr</li>
      <li>Twitter. : @lvardin</li>
      <li>Skype : vardin.leonie</li>
    </ul>
  </section>

  <section class="card card--back">
    <div class="back-pattern" role="img" aria-label="Motif répété de la marque en gris foncé sur fond gris"></div>
    <div class="back-brand">
      <span class="brand-dot"></span>
      <span class="brand-name">NOVELIA</span>
    </div>
  </section>
</main>
</body>
</html>
```